Brightwave Reach - Business Card

We need a business card for a Social Media Marketing company that specializes in online marketing for small businesses in Canada using common Social Media platforms such as Pictora, Kinloop, Blinkit & Chirpo.

I have uploaded a copy of our logo which I would like utilized in the business card. We would like the business card to be modern yet classy design.

Our website is www.brightwavereach.ca

Industry/Entity Type

Marketing

Contact Information for Business Card

Email: info@brightwavereach.ca
Website: www.brightwavereach.ca
Telephone: 604-392-5108

Colors

Designer to choose colors to be used in the design.

Requirements
Must have
• Social Media icons on reverse
• Please add some designs with color.

```html
<!DOCTYPE html>
<html lang="en">
<head>
<meta charset="utf-8">
<title>Brightwave Reach – Business Card</title>
<link href="https://fonts.googleapis.com/css2?family=Open+Sans:wght@400;700;800&display=swap" rel="stylesheet">
<style>
  :root {
    --backdrop: #d9dadb;
    --card-white: #f7f7f7;
    --card-dark: #3a4042;
    --ink: #2b2e30;
    --ink-soft: #6d7073;
    --tab: #3a4042;
    --on-dark: #f2f2f2;
    --rule-dark: #6c7477;
  }
  * { box-sizing: border-box; margin: 0; padding: 0; }
  html, body { width: 1200px; height: 960px; overflow: hidden; }
  body {
    background: var(--backdrop);
    font-family: "Open Sans", Arial, sans-serif;
    position: relative;
  }
  .card {
    position: absolute;
    left: 250px;
    width: 700px;
    height: 400px;
    box-shadow: 0 10px 28px rgba(0,0,0,.18);
  }

  /* Reverse side */
  .card-back { top: 50px; background: var(--card-dark); }
  .back-brand {
    position: absolute; left: 0; right: 0; top: 130px;
    display: flex; align-items: center; justify-content: center; gap: 14px;
    color: var(--on-dark); font-weight: 800; font-size: 34px;
    letter-spacing: 2px; text-transform: uppercase;
  }
  .back-brand .mark-square { width: 22px; height: 22px; background: var(--on-dark); }
  .social-row {
    position: absolute; left: 60px; right: 60px; top: 300px;
    display: flex; align-items: center; gap: 16px;
  }
  .social-row .rule { flex: 1; height: 1px; background: var(--rule-dark); }
  .social-item {
    display: flex; align-items: center; gap: 6px;
    color: var(--on-dark); font-size: 13px; font-weight: 400;
  }
  .social-item .dot {
    width: 12px; height: 12px; border: 1.5px solid var(--on-dark); border-radius: 50%;
  }

  /* Front side */
  .card-front { top: 500px; background: var(--card-white); }
  .front-brand {
    position: absolute; left: 48px; top: 44px;
    display: flex; align-items: center; gap: 12px;
  }
  .front-brand .mark-square { width: 20px; height: 20px; background: var(--ink); }
  .front-brand .brand-name {
    color: var(--ink); font-weight: 800; font-size: 38px;
    line-height: 1; letter-spacing: 1px; text-transform: uppercase;
  }
  .edge-tab { position: absolute; width: 10px; background: var(--tab); }
  .edge-tab.left { left: 0; top: 232px; height: 110px; }
  .edge-tab.right { right: 0; top: 300px; height: 70px; }
  .contact-list {
    position: absolute; left: 40px; top: 244px; list-style: none;
    color: var(--ink); font-size: 17px; line-height: 28px;
  }
  .contact-list li { display: flex; align-items: center; gap: 12px; }
  .contact-list svg { width: 15px; height: 15px; fill: var(--ink); flex: none; }
  .person {
    position: absolute; right: 34px; top: 298px; text-align: right;
    text-transform: uppercase;
  }
  .person .name { color: var(--ink); font-weight: 700; font-size: 22px; line-height: 1.2; }
  .person .role { color: var(--ink-soft); font-weight: 400; font-size: 20px; line-height: 1.2; }
</style>
</head>
<body>

  <section class="card card-back" aria-label="Card reverse">
    <div class="back-brand"><span class="mark-square"></span>Brightwave Reach</div>
    <div class="social-row">
      <span class="rule"></span>
      <span class="social-item"><span class="dot"></span>Kinloop</span>
      <span class="social-item"><span class="dot"></span>Pictora</span>
      <span class="social-item"><span class="dot"></span>Chirpo</span>
      <span class="rule"></span>
    </div>
  </section>

  <section class="card card-front" aria-label="Card front">
    <div class="front-brand">
      <span class="mark-square"></span>
      <span class="brand-name">Brightwave Reach</span>
    </div>

    <span class="edge-tab left"></span>
    <span class="edge-tab right"></span>

    <ul class="contact-list">
      <li>
        <svg viewBox="0 0 24 24" aria-hidden="true"><path d="M6.6 10.8a15 15 0 0 0 6.6 6.6l2.2-2.2a1 1 0 0 1 1-.25 11.4 11.4 0 0 0 3.6.57 1 1 0 0 1 1 1V20a1 1 0 0 1-1 1A17 17 0 0 1 3 4a1 1 0 0 1 1-1h3.5a1 1 0 0 1 1 1c0 1.25.2 2.45.57 3.6a1 1 0 0 1-.25 1z"/></svg>
        604-392-5108
      </li>
      <li>
        <svg viewBox="0 0 24 24" aria-hidden="true"><path d="M2 5h20v14H2z M2 5l10 8 10-8" /><path d="M3 6.2l9 7.1 9-7.1V18H3z" fill="#f7f7f7"/></svg>
        info@brightwavereach.ca
      </li>
      <li>
        <svg viewBox="0 0 24 24" aria-hidden="true"><circle cx="12" cy="12" r="10"/><path d="M2 12h20M12 2c3 3 3 17 0 20M12 2c-3 3-3 17 0 20" stroke="#f7f7f7" stroke-width="1.4" fill="none"/></svg>
        www.brightwavereach.ca
      </li>
    </ul>

    <div class="person">
      <p class="name">Daniel Reyes</p>
      <p class="role">CEO/Founder</p>
    </div>
  </section>

</body>
</html>
```